Harbor of Kitchencraft Podcast Episode Cover

I’m looking for a clean, professional, and eye-catching podcast episode cover template for my show, Harbor of Kitchencraft. Each week, I feature a new guest, so the design must allow me (or my team) to easily swap in a new guest’s photo without needing advanced design skills.

The template should be:

- Drag-and-drop friendly: simple for me to replace the guest’s headshot in Canva, Photoshop, or similar.
- On-brand with the Harbor of Kitchencraft podcast: professional yet approachable, foodservice industry-focused.
- Bold and attention-grabbing for podcast platforms and social media.

Readable text at small sizes, since covers are often viewed as thumbnails.

Design Elements to Include:

1. Podcast Title: “Harbor of Kitchencraft” (prominently displayed)
2. Subtitle/Space: Line for guest’s name, professional title, and company name
3. Photo Placeholder: Large, central area where I can easily drag and drop a guest photo
4. Brand Colors: attached
5. Clean, modern fonts (easy to read at thumbnail size)
6. Background graphics or patterns that give a sense of foodservice, leadership, or nationwide reach... but do not overpower the guest photo

Format Requirements:

- Editable source file (PSD, Canva template, or layered AI/INDD)
- JPG/PNG exports for immediate use
- Square format (3000x3000px) for podcast platforms

Style Inspiration:
Think modern podcast covers: bold fonts, clean lines, professional with a touch of energy.

Deliverables:

1. Final episode cover template (editable file)
2. Instructions or guidance on how to swap out guest photos

```html
<!DOCTYPE html>
<html lang="en">
<head>
<meta charset="utf-8">
<title>Harbor of Kitchencraft – Episode Cover Templates</title>
<link rel="stylesheet" href="https://fonts.googleapis.com/css2?family=Archivo+Black&family=Roboto:wght@700&display=swap">
<style>
  :root {
    --navy: #1d3750;
    --gold: #f6b51a;
    --white: #ffffff;
    --page: #ffffff;
    --photo-warm: #d9b892;
    --photo-cool: #5e6066;
    --photo-dark: #2a2a2c;
  }
  * { margin: 0; padding: 0; box-sizing: border-box; }
  html, body {
    width: 1164px;
    height: 1200px;
    overflow: hidden;
    background: var(--page);
  }
  .canvas {
    position: relative;
    width: 1164px;
    height: 1200px;
  }
  .cover {
    position: absolute;
    top: 354px;
    width: 487px;
    height: 487px;
    overflow: hidden;
    box-shadow: 0 14px 22px rgba(0, 0, 0, 0.18);
  }
  .cover--light { left: 57px; }
  .cover--dark { left: 617px; }
  .cover__backdrop {
    position: absolute;
    inset: 0;
    width: 100%;
    height: 100%;
  }
  .show-title {
    position: absolute;
    left: 30px;
    top: 40px;
    font-family: "Archivo Black", sans-serif;
    font-weight: 400;
    font-size: 21px;
    line-height: 1;
    letter-spacing: 0.5px;
    color: var(--white);
    white-space: nowrap;
  }
  .guest-photo {
    position: absolute;
    left: 134px;
    top: 134px;
    width: 214px;
    height: 214px;
    border-radius: 50%;
    border: 4px solid var(--white);
    background:
      radial-gradient(circle at 48% 40%, var(--photo-warm) 0 22%, transparent 40%),
      linear-gradient(180deg, var(--photo-cool) 0%, #8a7f72 45%, var(--photo-dark) 78%, var(--photo-dark) 100%);
  }
  .guest-info {
    position: absolute;
    left: 0;
    right: 0;
    top: 366px;
    text-align: center;
    padding-left: 8px;
  }
  .guest-name {
    font-family: "Archivo Black", sans-serif;
    font-size: 32px;
    line-height: 1;
    letter-spacing: 0.5px;
  }
  .guest-role {
    margin-top: 6px;
    font-family: "Roboto", sans-serif;
    font-weight: 700;
    font-size: 10.5px;
    letter-spacing: 2.4px;
  }
  .cover--light .guest-name,
  .cover--light .guest-role { color: var(--navy); }
  .cover--dark .guest-name,
  .cover--dark .guest-role { color: var(--white); }
</style>
</head>
<body>
<main class="canvas">

  <section class="cover cover--light" aria-label="Episode cover, light variant">
    <svg class="cover__backdrop" viewBox="0 0 366 366" preserveAspectRatio="none" aria-hidden="true">
      <rect width="366" height="366" fill="var(--navy)"/>
      <polygon points="366,46 366,366 44,366" fill="var(--white)"/>
      <polygon points="322,0 366,0 366,46 44,366 0,366 0,322" fill="var(--gold)"/>
    </svg>
    <h1 class="show-title">HARBOR OF KITCHENCRAFT</h1>
    <div class="guest-photo" role="img" aria-label="Guest headshot placeholder"></div>
    <div class="guest-info">
      <p class="guest-name">MARCUS DALE</p>
      <p class="guest-role">CHIEF MARKETING OFFICER</p>
    </div>
  </section>

  <section class="cover cover--dark" aria-label="Episode cover, dark variant">
    <svg class="cover__backdrop" viewBox="0 0 366 366" preserveAspectRatio="none" aria-hidden="true">
      <rect width="366" height="366" fill="var(--navy)"/>
      <polygon points="322,0 366,0 366,46 44,366 0,366 0,322" fill="var(--gold)"/>
    </svg>
    <h1 class="show-title">HARBOR OF KITCHENCRAFT</h1>
    <div class="guest-photo" role="img" aria-label="Guest headshot placeholder"></div>
    <div class="guest-info">
      <p class="guest-name">MARCUS DALE</p>
      <p class="guest-role">CHIEF MARKETING OFFICER</p>
    </div>
  </section>

</main>
</body>
</html>
```